Granite Path Fitness Presents Harbor Touch Massage with Marguerite

I'm promoting my massage therapy business which is located in a personal one on one training gym. A few of the modalities I offer are:
Basic Relaxation -light or deep.
Medical Massage- specific work for a specific problem.
Reflexology- feet feet and more feet.
Thai Yoga- I stretch you.
Scalp and Feet- Mega tension relief.
For more details, information and to make an appointment call Marguerite at :731 528 4170. E mail: tulipbaker@mailvex.com
I was playing with this: Bring me your tired, aching, stressed-out body and give me a chance to work some magic. (I hate promoting myself and that was extreme for me.)

Target Market(s)

Gym members and walk-ins from the Uptown Kingston, NY neighborhood.

Industry/Entity Type

Business

Colors

Designer to choose colors to be used in the design.

Requirements
Must have
• My name and phone # and my e mail address.
Should not have
• Anything sexual. This is serious healing work done by a licenced professional so there can be no confusion as to intent.

```html
<!DOCTYPE html>
<html lang="en">
<head>
<meta charset="utf-8">
<title>Harbor Touch Massage Flyer</title>
<link rel="stylesheet" href="https://fonts.googleapis.com/css2?family=Source+Sans+3:wght@400;600;700&family=Roboto+Condensed:ital,wght@0,700;1,300&display=swap">
<style>
  :root {
    --lavender: #6c69ad;
    --lavender-dark: #5f5c9f;
    --page: #ffffff;
    --mist-light: #e9e9ec;
    --mist-mid: #c9c9ce;
    --mist-dark: #a9a9b0;
    --skin-light: #e4e2e2;
    --skin-mid: #9c9a9a;
    --ache: #e2806f;
    --trim: #bdbdc2;
    --white: #ffffff;
  }
  * { margin: 0; padding: 0; box-sizing: border-box; }
  html, body { width: 1200px; height: 1200px; overflow: hidden; background: var(--page); }
  .canvas { position: relative; width: 1200px; height: 1200px; background: var(--page); }

  .crop-marks { position: absolute; inset: 0; }

  .flyer {
    position: absolute; left: 232px; top: 84px; width: 735px; height: 1032px;
    overflow: hidden;
    border: 1px solid var(--trim);
  }
  .flyer-backdrop {
    position: absolute; inset: 0;
    background:
      radial-gradient(ellipse 60% 25% at 30% 8%, rgba(255,255,255,.55), transparent 70%),
      radial-gradient(ellipse 70% 20% at 50% 72%, rgba(255,255,255,.6), transparent 70%),
      linear-gradient(180deg, var(--mist-mid) 0%, var(--mist-light) 22%, var(--mist-mid) 48%, var(--mist-light) 66%, var(--mist-mid) 100%);
  }
  .inner-frame {
    position: absolute; left: 11px; top: 10px; right: 11px; bottom: 0;
    border: 1px solid rgba(150,150,158,.6); border-bottom: none;
  }

  .headline {
    position: absolute; left: 122px; top: 68px; width: 560px;
    font-family: "Source Sans 3", sans-serif; font-weight: 700;
    font-size: 26px; line-height: 45.5px; color: var(--lavender);
  }

  .relief-grid { position: absolute; left: 46px; top: 234px; width: 644px; height: 322px; background: var(--white); }
  .relief-photo { position: absolute; }
  .relief-photo.knee      { left: 0;     top: 0;   width: 143px; height: 170px; background: radial-gradient(circle at 40% 60%, var(--ache), var(--skin-mid) 60%, var(--skin-light)); }
  .relief-photo.upperback { left: 143px; top: 0;   width: 349px; height: 170px; background: radial-gradient(ellipse 40% 45% at 50% 60%, var(--ache), var(--skin-mid) 70%, var(--white)); }
  .relief-photo.elbow     { left: 492px; top: 0;   width: 152px; height: 170px; background: radial-gradient(circle at 50% 30%, var(--ache), var(--skin-mid) 55%, #5a5a5a); }
  .relief-photo.shoulder  { left: 0;     top: 170px; width: 143px; height: 152px; background: radial-gradient(circle at 30% 45%, var(--ache), var(--skin-mid) 60%, var(--white)); }
  .relief-photo.lowerback { left: 146px; top: 170px; width: 340px; height: 152px; background: radial-gradient(ellipse 30% 50% at 50% 70%, var(--ache), var(--skin-mid) 70%, var(--white)); }
  .relief-photo.neck      { left: 506px; top: 170px; width: 138px; height: 152px; background: radial-gradient(circle at 45% 20%, var(--ache), transparent 25%), radial-gradient(circle at 35% 85%, var(--ache), var(--skin-mid) 40%, var(--white) 75%); }

  .title-band {
    position: absolute; left: 120px; top: 580px; width: 496px; height: 49px;
    background: var(--lavender);
    display: flex; align-items: center; justify-content: center;
    font-family: "Source Sans 3", sans-serif; font-weight: 600;
    font-size: 17px; color: var(--white);
  }

  .services { position: absolute; left: 104px; top: 690px; list-style: none; }
  .service { display: flex; height: 33.6px; align-items: center; }
  .service-name {
    width: 174px; font-family: "Roboto Condensed", sans-serif; font-weight: 700;
    font-size: 21px; color: var(--lavender);
  }
  .service-note {
    font-family: "Roboto Condensed", sans-serif; font-weight: 300; font-style: italic;
    font-size: 21px; color: var(--lavender);
  }

  .contact-band { position: absolute; left: 0; bottom: 0; width: 735px; height: 122px; }
  .contact-band .band-shape { position: absolute; left: 0; top: 0; }
  .contact-lead {
    position: absolute; left: 0; top: 38px; width: 100%; text-align: center;
    font-family: "Source Sans 3", sans-serif; font-weight: 600;
    font-size: 12px; color: var(--white); letter-spacing: .1px;
  }
  .contact-line {
    position: absolute; left: 158px; top: 58px; display: flex; align-items: center;
    font-family: "Source Sans 3", sans-serif; color: var(--white); white-space: nowrap;
  }
  .contact-line .phone-icon { flex: none; display: block; }
  .contact-line .call-label { font-size: 14px; margin-left: 6px; }
  .contact-line .phone-number { font-size: 22px; margin-left: 6px; letter-spacing: .3px; }
  .contact-line .mail-icon { flex: none; display: block; margin-left: 12px; }
  .contact-line .email { font-size: 14px; margin-left: 8px; }
</style>
</head>
<body>
<div class="canvas">

  <svg class="crop-marks" width="1200" height="1200" aria-hidden="true">
    <g stroke="#9a9a9a" stroke-width="1">
      <line x1="244" y1="30" x2="244" y2="72"/>
      <line x1="956" y1="30" x2="956" y2="72"/>
      <line x1="244" y1="1128" x2="244" y2="1170"/>
      <line x1="956" y1="1128" x2="956" y2="1170"/>
      <line x1="178" y1="94" x2="220" y2="94"/>
      <line x1="980" y1="94" x2="1022" y2="94"/>
      <line x1="178" y1="1106" x2="220" y2="1106"/>
      <line x1="980" y1="1106" x2="1022" y2="1106"/>
    </g>
  </svg>

  <article class="flyer">
    <div class="flyer-backdrop" role="img" aria-label="Soft black and white photo of a massage therapist's hands at work in a calm treatment room"></div>
    <div class="inner-frame"></div>

    <h1 class="headline">Bring me your tired,<br>aching, stressed-out body and<br>give me a chance to work some magic.</h1>

    <div class="relief-grid">
      <div class="relief-photo knee" role="img" aria-label="Hands holding a sore knee with a red glow of pain"></div>
      <div class="relief-photo upperback" role="img" aria-label="Hands pressing the tense upper back and shoulders"></div>
      <div class="relief-photo elbow" role="img" aria-label="Hand gripping an aching elbow"></div>
      <div class="relief-photo shoulder" role="img" aria-label="Hand on a painful shoulder"></div>
      <div class="relief-photo lowerback" role="img" aria-label="Hands on an aching lower back"></div>
      <div class="relief-photo neck" role="img" aria-label="Back view with pain spots at the neck and lower back"></div>
    </div>

    <div class="title-band">Granite Path Fitness Presents Harbor Touch Massage</div>

    <ul class="services">
      <li class="service"><span class="service-name">Basic Relaxation</span><span class="service-note">- light or deep.</span></li>
      <li class="service"><span class="service-name">Medical Massage</span><span class="service-note">- specific work for a specific problem.</span></li>
      <li class="service"><span class="service-name">Reflexology</span><span class="service-note">- feet feet and more feet.</span></li>
      <li class="service"><span class="service-name">Thai Yoga</span><span class="service-note">- I stretch you.</span></li>
      <li class="service"><span class="service-name">Scalp and Feet</span><span class="service-note">- mega tension relief.</span></li>
    </ul>

    <footer class="contact-band">
      <svg class="band-shape" width="735" height="122" aria-hidden="true">
        <path d="M0 58 Q367 -28 735 58 L735 122 L0 122 Z" fill="var(--lavender)"/>
      </svg>
      <p class="contact-lead">FOR MORE DETAILS, INFORMATION AND TO MAKE AN APPOINTMENT</p>
      <div class="contact-line">
        <svg class="phone-icon" width="20" height="34" viewBox="0 0 20 34" aria-hidden="true">
          <path d="M6 2 C2 4 1 10 2 17 C3 24 6 30 10 32 L13 30 L9 22 L6 23 C5 19 5 14 6 11 L9 11 L10 3 Z" fill="var(--white)"/>
        </svg>
        <span class="call-label">call Marguerite at:</span>
        <span class="phone-number">731 528 4170</span>
        <svg class="mail-icon" width="30" height="20" viewBox="0 0 30 20" aria-hidden="true">
          <rect x="1" y="1" width="28" height="18" fill="none" stroke="var(--white)" stroke-width="2"/>
          <path d="M1 1 L15 12 L29 1 M1 19 L11 9 M29 19 L19 9" fill="none" stroke="var(--white)" stroke-width="2"/>
        </svg>
        <span class="email">tulipbaker@mailvex.com</span>
      </div>
    </footer>
  </article>
</div>
</body>
</html>
```